Business Card Design Project 4 Construction Business

I am after a creative, but sleek and simple/ clean business card design. This design will form the basis of future items and might include a logo or simply a creative way to lay out the text of my company name 'kestrel ventures'
I like the simplicity of black and white however I would also be happy to see a splash of colour introduced somehow to give the text some interest and make it stand out.
I would like a double sided card.
I am young (ish!) and professional, offering construction and project management services, what I don't want is the traditional builders type card featuring a cheesy hammer/ saw image etc.
As the company name, kestrel ventures, suggests, we focus on working closely and collaboratively together, in synergy with all stakeholders involved in the projects that we undertake
Construction

```html
<!DOCTYPE html>
<html lang="en">
<head>
<meta charset="utf-8">
<title>Kestrel Ventures – Business Cards</title>
<link rel="stylesheet" href="https://fonts.googleapis.com/css2?family=Play:wght@400;700&family=Saira:wght@300;400&display=swap">
<style>
  :root {
    --page: #ffffff;
    --lime: #a8f20c;
    --lime-text: #b6f23a;
    --ink: #0c0c0c;
    --white: #ffffff;
    --grey-text: #c9c9c9;
    --dark-centre: #2b2b2b;
    --dark-edge: #000000;
  }
  * { margin: 0; padding: 0; box-sizing: border-box; }
  html, body {
    width: 1200px;
    height: 619px;
    overflow: hidden;
    background: var(--page);
  }
  .sheet {
    position: relative;
    width: 1200px;
    height: 619px;
  }
  .card {
    position: absolute;
    top: 0;
    width: 393px;
    height: 607px;
    overflow: hidden;
  }
  .card--lime { left: 0; background: var(--lime); }
  .card--dark {
    background: radial-gradient(ellipse 70% 55% at 50% 40%, var(--dark-centre) 0%, #141414 55%, var(--dark-edge) 100%);
  }
  .card--contact-dark { left: 404px; width: 392px; }
  .card--brand { left: 806px; width: 394px; }

  .contact {
    position: absolute;
    right: 62px;
    top: 132px;
    text-align: right;
    font-family: "Saira", sans-serif;
    font-weight: 300;
  }
  .contact__name {
    font-family: "Play", sans-serif;
    font-size: 25px;
    line-height: 30px;
    font-weight: 400;
  }
  .contact__role {
    font-family: "Play", sans-serif;
    font-size: 19px;
    line-height: 24px;
    margin-bottom: 16px;
  }
  .contact__address p {
    font-size: 16px;
    line-height: 26px;
  }
  .contact__phone {
    font-size: 16px;
    line-height: 26px;
    margin-top: 17px;
  }
  .contact__line {
    font-size: 14.5px;
    line-height: 26px;
  }
  .card--lime .contact__name { color: var(--ink); }
  .card--lime .contact__role { color: var(--white); }
  .card--lime .contact__address,
  .card--lime .contact__phone,
  .card--lime .contact__line { color: var(--ink); }
  .card--contact-dark .contact__name,
  .card--contact-dark .contact__role { color: var(--lime-text); }
  .card--contact-dark .contact__address,
  .card--contact-dark .contact__phone,
  .card--contact-dark .contact__line { color: var(--grey-text); }

  .brand {
    position: absolute;
    left: 0;
    right: 0;
    top: 122px;
    text-align: center;
  }
  .brand__name {
    font-family: "Saira", sans-serif;
    font-weight: 300;
    font-size: 58px;
    line-height: 66px;
    letter-spacing: 1px;
    color: #d0d0d0;
  }
  .brand__sub {
    font-family: "Saira", sans-serif;
    font-weight: 300;
    font-size: 27px;
    line-height: 32px;
    letter-spacing: 1px;
    color: #a8a8a8;
  }
  .brand__tagline {
    font-family: "Saira", sans-serif;
    font-weight: 300;
    font-size: 16px;
    line-height: 20px;
    color: var(--grey-text);
    margin-top: 36px;
  }

  .skyline {
    position: absolute;
    left: 64px;
    top: 436px;
    width: 268px;
    height: 94px;
  }
  .card--lime .skyline {
    background: linear-gradient(to bottom, rgba(255,255,255,0.55), rgba(255,255,255,0));
  }
  .card--dark .skyline {
    background: linear-gradient(to bottom, rgba(168,242,12,0.45), rgba(168,242,12,0));
  }
</style>
</head>
<body>
<main class="sheet">
  <section class="card card--lime">
    <div class="contact">
      <h1 class="contact__name">Lachlan Reeves</h1>
      <p class="contact__role">Director</p>
      <div class="contact__address">
        <p>18 Corella St</p>
        <p>Artarmon</p>
        <p>NSW 2064</p>
      </div>
      <p class="contact__phone">0412 555 019</p>
      <p class="contact__line">lachlan@kestrelventuresgroup.com.au</p>
      <p class="contact__line">www.kestrelventuresgroup.com.au</p>
    </div>
    <div class="skyline" role="img" aria-label="City skyline line illustration"></div>
  </section>

  <section class="card card--dark card--contact-dark">
    <div class="contact">
      <h2 class="contact__name">Lachlan Reeves</h2>
      <p class="contact__role">Director</p>
      <div class="contact__address">
        <p>18 Corella St</p>
        <p>Artarmon</p>
        <p>NSW 2064</p>
      </div>
      <p class="contact__phone">0412 555 019</p>
      <p class="contact__line">lachlan@kestrelventuresgroup.com.au</p>
      <p class="contact__line">www.kestrelventuresgroup.com.au</p>
    </div>
    <div class="skyline" role="img" aria-label="City skyline line illustration"></div>
  </section>

  <section class="card card--dark card--brand">
    <div class="brand">
      <p class="brand__name">KESTREL</p>
      <p class="brand__sub">VENTURES</p>
      <p class="brand__tagline">Construction &amp; Project Management</p>
    </div>
    <div class="skyline" role="img" aria-label="City skyline line illustration"></div>
  </section>
</main>
</body>
</html>
```